2 Page Business Flyer for Finance Business

Need a two page flyer created for a finance business. Lots of text and needs to fit on two pages.

Corporate business/banking look and feel. Not too many large images. Lots of white space, clean design. Attached is color palette and the text contents of the flyer.

```html
<!DOCTYPE html>
<html lang="en">
<head>
<meta charset="utf-8">
<title>Vanilla Options – Two Page Flyer</title>
<link href="https://fonts.googleapis.com/css2?family=Quicksand:wght@600;700&family=PT+Sans:wght@400;700&display=swap" rel="stylesheet">
<style>
  :root{
    --red:#c8413f;
    --red-light:#de6f6b;
    --red-pale:#f1c9c6;
    --ink:#2f2f2f;
    --body:#3a3a3a;
    --paper:#ffffff;
    --backdrop:#ece7e2;
  }
  *{box-sizing:border-box;margin:0;padding:0}
  html,body{width:1200px;height:800px;overflow:hidden;background:var(--backdrop)}
  body{position:relative;font-family:"PT Sans",Arial,sans-serif;color:var(--body)}
  .page{position:absolute;top:20px;width:537px;height:760px;background:var(--paper);overflow:hidden;box-shadow:0 2px 10px rgba(0,0,0,.12)}
  .page--front{left:43px}
  .page--back{left:620px}
  .hero{position:absolute;left:0;top:0;width:100%}
  .hero-photo{position:absolute;left:0;top:0;width:100%}
  .page--front .hero-photo{height:215px;background:linear-gradient(135deg,#3b3b3d 0%,#8a8d93 35%,#dfe3e8 60%,#b9b2ab 100%)}
  .page--back .hero-photo{height:130px;background:linear-gradient(120deg,#b8302f 0%,#c8413f 45%,#a52b2a 100%)}
  .hero-wave{position:absolute;left:0;top:0;width:100%}
  h2{font-family:"Quicksand",Arial,sans-serif;font-weight:700;color:var(--ink);font-size:13px;letter-spacing:.1px}
  h3{font-family:"PT Sans",Arial,sans-serif;font-weight:700;color:var(--ink);font-size:9.5px;margin:5px 0 3px}
  p{font-size:7.9px;line-height:10.6px;margin-bottom:6px}
  .content{position:absolute;left:28px;right:38px}
  .ticks{list-style:none;margin:5px 0 4px}
  .ticks li{position:relative;padding-left:22px;font-size:7.9px;line-height:10px;margin-bottom:5.2px}
  .ticks svg{position:absolute;left:3px;top:0;width:9px;height:9px}
  .panel{position:absolute;border:1px solid var(--red);border-radius:6px;padding:18px 14px 8px}
  .panel-title{position:absolute;top:-9px;left:50%;transform:translateX(-50%);background:var(--paper);padding:0 8px;font-family:"Quicksand",Arial,sans-serif;font-weight:700;font-size:12.5px;color:var(--ink);white-space:nowrap}
  .panel p{text-align:center;margin:0}
  .footer{position:absolute;left:0;bottom:0;width:100%;height:80px}
  .footer svg.wave{position:absolute;left:0;top:0;width:100%;height:80px}
  .contact{position:absolute;left:0;right:0;bottom:12px;display:flex;justify-content:center;align-items:center;gap:10px;color:#fff;font-family:"Quicksand",Arial,sans-serif;font-weight:700;font-size:15px}
  .contact svg{width:14px;height:14px;vertical-align:-2px;margin-right:5px}
  .divider{width:1px;height:18px;background:#fff;opacity:.9}
</style>
</head>
<body>

<svg width="0" height="0" style="position:absolute">
  <symbol id="tick" viewBox="0 0 10 10">
    <circle cx="5" cy="5" r="4" fill="none" stroke="#c8413f" stroke-width="1"/>
    <path d="M3 5.1 L4.6 6.6 L9.4 1.6" fill="none" stroke="#c8413f" stroke-width="1.2" stroke-linecap="round"/>
  </symbol>
  <symbol id="phone" viewBox="0 0 24 24">
    <path fill="#fff" d="M6.6 10.8a15 15 0 0 0 6.6 6.6l2.2-2.2c.3-.3.7-.4 1-.2 1.1.4 2.3.6 3.6.6.6 0 1 .4 1 1V20c0 .6-.4 1-1 1A17 17 0 0 1 3 4c0-.6.4-1 1-1h3.5c.6 0 1 .4 1 1 0 1.3.2 2.5.6 3.6.1.3 0 .7-.2 1z"/>
  </symbol>
  <symbol id="globe" viewBox="0 0 24 24">
    <g fill="none" stroke="#fff" stroke-width="2"><circle cx="12" cy="12" r="9"/><ellipse cx="12" cy="12" rx="4" ry="9"/><path d="M3 12h18M5 7h14M5 17h14"/></g>
  </symbol>
</svg>

<!-- Front page -->
<section class="page page--front">
  <div class="hero">
    <div class="hero-photo" role="img" aria-label="Photo of hands pointing a pen at financial charts on a clipboard beside a laptop"></div>
    <svg class="hero-wave" viewBox="0 0 537 260" height="260" preserveAspectRatio="none">
      <path d="M0 200 C150 250 330 150 537 175 L537 260 L0 260 Z" fill="#c8413f"/>
      <path d="M0 218 C170 262 340 175 537 190 L537 260 L0 260 Z" fill="#e9a29e"/>
      <path d="M0 226 C170 268 340 185 537 198 L537 260 L0 260 Z" fill="#ffffff"/>
    </svg>
  </div>

  <div class="content" style="top:232px">
    <h2>How does a Vanilla Option contract work?</h2>
    <p style="margin-top:8px">The buyer of a vanilla option receives protection against an adverse movement in the exchange rate while allowing full participation in a beneficial move. At no time is the buyer of a Vanilla Option obligated to exercise the Option and transact the currencies, therefore providing flexibility in cases where the requirement to purchase foreign currency is not certain.</p>
    <p>A buyer of vanilla options is required to pay a premium (like an insurance premium) for the right, but not the obligation, to exchange currency at a predetermined rate on a predetermined date.</p>
    <ul class="ticks">
      <li><svg><use href="#tick"/></svg>Set a protection rate which will be your worst-case scenario at expiry</li>
      <li><svg><use href="#tick"/></svg>Determine the amount of currency you wish to protect</li>
      <li><svg><use href="#tick"/></svg>Choose an expiry date for the contract</li>
      <li><svg><use href="#tick"/></svg>Calculate the premium you are required to pay</li>
    </ul>
    <h3>Let’s look at an example: You are in importer.</h3>
    <p>Your construction company has bid on a project that if successful, will require you to import materials from the United States to use in construction. You have used todays pricing of materials in calculating your bid and want to protect against an adverse move in the US dollar exchange rate from eroding your margin if your bid is chosen for the project.</p>
    <p>You choose to buy a Vanilla Call which will protect you from a rise in the USD/CAD exchange rate above your protection rate. You choose to buy protection on $500,000 USD, with a protection rate (strike rate) of 1.3300 expiring 3 months from now. You are required to pay a premium which in this case is calculated to be 1.8%, or 11,970 CAD.</p>
    <p>Your bid is successful: If the exchange rate is below your protection rate at expiration, you have no obligation relating to the vanilla call and you are free to buy USD at the cheaper spot rate. If the exchange rate is above your protection rate, you have the right to purchase your USD at the protection rate, and thereby claiming your insurance policy.</p>
    <p>Your bid is not successful: You have no obligation relating to the vanilla option however, if at expiry the exchange rate is above the protection rate, you may exercise your right to buy USD at the lower rate and simultaneous sell USD back at the prevailing spot rate, thereby recouping some or all of the premium paid to buy the option. Alternatively, if you find out your bid was not successful with time still left until expiration, you may sell your option back into the market in the case that it still has residual value, which will depend on various market factors.</p>
  </div>

  <div class="panel" style="left:69px;top:592px;width:391px;height:88px">
    <span class="panel-title">Characteristics :</span>
    <ul class="ticks" style="margin:0">
      <li><svg><use href="#tick"/></svg>You are looking for a straight-forward hedging solution</li>
      <li><svg><use href="#tick"/></svg>You want to receive full benefit from an appreciation of the currency you are exposed to</li>
      <li><svg><use href="#tick"/></svg>You are comfortable receiving protection at the strike rate of the option</li>
      <li><svg><use href="#tick"/></svg>You are willing to pay the non-refundable premium</li>
    </ul>
  </div>

  <footer class="footer">
    <svg class="wave" viewBox="0 0 537 80" preserveAspectRatio="none">
      <path d="M0 25 C170 -5 360 45 537 2 L537 80 L0 80 Z" fill="#e9a29e"/>
      <path d="M0 30 C170 2 360 50 537 10 L537 80 L0 80 Z" fill="#ffffff"/>
      <path d="M0 34 C170 8 360 54 537 16 L537 80 L0 80 Z" fill="#c8413f"/>
    </svg>
    <div class="contact">
      <span><svg><use href="#phone"/></svg>0123-456789</span>
      <span class="divider"></span>
      <span><svg><use href="#globe"/></svg>www.northvalefx.com</span>
    </div>
  </footer>
</section>

<!-- Back page -->
<section class="page page--back">
  <div class="hero">
    <div class="hero-photo" role="img" aria-label="Red-tinted photo of business people in an office meeting"></div>
    <svg class="hero-wave" viewBox="0 0 537 170" height="170" preserveAspectRatio="none">
      <path d="M0 100 C150 140 330 60 537 100 L537 170 L0 170 Z" fill="#c8413f"/>
      <path d="M0 112 C160 150 340 75 537 108 L537 170 L0 170 Z" fill="#e9a29e"/>
      <path d="M0 118 C160 156 340 84 537 116 L537 170 L0 170 Z" fill="#ffffff"/>
    </svg>
  </div>

  <div class="panel" style="left:104px;top:150px;width:329px;height:88px">
    <span class="panel-title">Advantages:</span>
    <ul class="ticks" style="margin:0">
      <li><svg><use href="#tick"/></svg>You hedge your foreign currency exposure at a predefined hedge rate</li>
      <li><svg><use href="#tick"/></svg>You can choose the hedge rate that suits your budget requirements</li>
      <li><svg><use href="#tick"/></svg>Provides the ability to fully participate in a favourable exchange rate move</li>
      <li><svg><use href="#tick"/></svg>You can choose from most major currency pairs to meet your needs</li>
    </ul>
  </div>

  <div class="panel" style="left:104px;top:261px;width:329px;height:56px;padding-top:19px">
    <span class="panel-title">Risks:</span>
    <p>Premium paid is non-refundable and remains your only obligation<br>when buying vanilla options</p>
  </div>

  <div class="content" style="top:334px;left:25px;right:40px">
    <h2>Why use Vanilla Options?</h2>
    <p style="margin-top:5px">Vanilla options are often compared to an insurance product. The buyer pays a non-refundable premium for the right, but not the obligation to trade currency in the future at the protection rate of the option. This product allows you to participate in a beneficial move to an unlimited extent, which will be the most advantageous outcome, if the exchange rate moves in your favour enough to more than offset the premium paid for the option.</p>
    <h2 style="margin-top:12px">What determines the price of a Vanilla Option?</h2>
    <p style="margin-top:5px">The cost of an option is defined by the premium that is required to be paid in order to enter into the contract. Premiums are calculated using the industry standard formulas based upon the Black Scholes model. The most important variables in the option pricing formulas include the following:</p>
    <ul class="ticks" style="margin-top:20px">
      <li><svg><use href="#tick"/></svg>The current market Spot Rate</li>
      <li><svg><use href="#tick"/></svg>Market volatility – the higher the volatility, the higher the premium.</li>
      <li><svg><use href="#tick"/></svg>The Term of the Option – a longer term typically results in a higher premium.</li>
      <li><svg><use href="#tick"/></svg>The Strike Rate – the closer to being ITM the protection rate is, the higher the premium.</li>
      <li><svg><use href="#tick"/></svg>The interest rate differential of the two currencies involved.</li>
      <li><svg><use href="#tick"/></svg>Style – European or American, or whether the option can be exercised prior to expiration</li>
    </ul>
  </div>

  <div class="panel" style="left:25px;top:586px;width:473px;height:80px;padding:20px 26px">
    <p>An option can either a European (meaning that they can only be exercised on the expiry date), or American (meaning that they can be exercised at any time prior to expiration). We normally deals in European options however, we do offer American options under certain circumstances and when specific delivery terms are agreed upon between us and the customer.</p>
  </div>

  <footer class="footer">
    <svg class="wave" viewBox="0 0 537 80" preserveAspectRatio="none">
      <path d="M0 25 C170 -5 360 45 537 2 L537 80 L0 80 Z" fill="#e9a29e"/>
      <path d="M0 30 C170 2 360 50 537 10 L537 80 L0 80 Z" fill="#ffffff"/>
      <path d="M0 34 C170 8 360 54 537 16 L537 80 L0 80 Z" fill="#c8413f"/>
    </svg>
    <div class="contact">
      <span><svg><use href="#phone"/></svg>0123-456789</span>
      <span class="divider"></span>
      <span><svg><use href="#globe"/></svg>www.northvalefx.com</span>
    </div>
  </footer>
</section>

</body>
</html>
```